Granger Earthworks LLC business card design

Excavation company business cards

Contact Information for Business Card

Granger Earthworks LLC cell phone 208-555-0147 office phone 208-555-0193 grangerearthworksllc@mailnest.example Driveways, site prep, retaining walls, septic systems, rock delivery

Colors

Designer to choose colors to be used in the design.

```html
<!DOCTYPE html>
<html lang="en">
<head>
<meta charset="utf-8">
<title>Granger Earthworks LLC – Business Card</title>
<link rel="stylesheet" href="https://fonts.googleapis.com/css2?family=Montserrat:ital,wght@0,600;0,700;0,800;1,500&family=Roboto:wght@400;500&display=swap">
<style>
  :root{
    --bg:#c9c9c9;
    --orange:#f26a1f;
    --ink:#1f1f1f;
    --ink-soft:#2b2b2b;
    --paper:#ffffff;
    --grey:#6d6d6d;
    --text-light:#f2f2f2;
  }
  *{box-sizing:border-box;margin:0;padding:0}
  html,body{width:1200px;height:788px;overflow:hidden}
  body{background:var(--bg);font-family:"Roboto",sans-serif;position:relative}

  .card{position:absolute;border-radius:22px;overflow:hidden;box-shadow:0 10px 30px rgba(0,0,0,.25)}

  /* Front */
  .card-front{left:80px;top:79px;width:360px;height:630px;background:var(--ink)}
  .front-top{position:absolute;left:0;top:0;width:100%;height:360px;background:var(--paper)}
  .brand{position:absolute;left:0;top:120px;width:100%;text-align:center;
    font-family:"Montserrat",sans-serif;font-weight:800;color:var(--orange);
    font-size:27px;line-height:1.15;letter-spacing:.5px;text-transform:uppercase}
  .person{position:absolute;left:0;top:262px;width:100%;text-align:center}
  .person-name{font-family:"Montserrat",sans-serif;font-weight:700;color:var(--orange);font-size:22px;letter-spacing:.5px}
  .person-role{font-family:"Montserrat",sans-serif;font-style:italic;font-weight:500;color:var(--ink);font-size:16px;margin-top:4px}
  .divider{position:absolute;left:0;top:359px;width:100%;height:2px;background:var(--orange)}
  .icon-row{position:absolute;top:343px;right:26px;display:flex;gap:8px}
  .icon{width:34px;height:34px;border-radius:50%;background:var(--orange);border:3px solid var(--paper);
    display:flex;align-items:center;justify-content:center}
  .icon svg{width:16px;height:16px;fill:none;stroke:var(--paper);stroke-width:2;stroke-linecap:round;stroke-linejoin:round}
  .contact{position:absolute;right:26px;top:400px;text-align:right;color:var(--text-light);font-size:15.5px;line-height:1.65}
  .rule{position:absolute;left:26px;right:26px;top:530px;height:2px;background:var(--orange)}
  .address{position:absolute;left:26px;top:548px;color:var(--text-light);font-size:15.5px;line-height:1.55}

  /* Back */
  .card-back{left:490px;top:214px;width:630px;height:360px;background:var(--ink)}
  .back-pattern{position:absolute;inset:0;
    background:linear-gradient(160deg,#4a4a4a 0%,#2e2e2e 45%,#1c1c1c 100%)}
  .back-brand{position:absolute;left:0;top:108px;width:100%;display:flex;align-items:center;justify-content:center;gap:10px;
    font-family:"Montserrat",sans-serif;font-weight:800;color:var(--orange);font-size:22px;text-transform:uppercase;letter-spacing:.5px}
  .back-brand .dot{width:14px;height:14px;border-radius:50%;background:var(--orange)}
  .services{position:absolute;left:0;bottom:58px;width:100%;text-align:center;color:var(--text-light);
    font-family:"Montserrat",sans-serif;font-weight:600;font-size:17px;line-height:1.7}
  .services li{display:inline;list-style:none;margin:0 9px}
  .services li::before{content:"";display:inline-block;width:6px;height:6px;border-radius:50%;background:var(--orange);margin-right:7px;vertical-align:middle}
</style>
</head>
<body>

<section class="card card-front" aria-label="Business card front">
  <div class="front-top"></div>
  <div class="brand">Granger<br>Earthworks LLC</div>
  <div class="person">
    <div class="person-name">DALE HARTLEY</div>
    <div class="person-role">Founder</div>
  </div>
  <div class="divider"></div>
  <div class="icon-row">
    <span class="icon"><svg viewBox="0 0 24 24"><path d="M5 3h4l2 5-3 2a12 12 0 0 0 6 6l2-3 5 2v4a2 2 0 0 1-2 2A17 17 0 0 1 3 5a2 2 0 0 1 2-2z"/></svg></span>
    <span class="icon"><svg viewBox="0 0 24 24"><rect x="7" y="2" width="10" height="20" rx="2"/><path d="M11 18h2"/></svg></span>
    <span class="icon"><svg viewBox="0 0 24 24"><rect x="3" y="5" width="18" height="14" rx="1"/><path d="M3 6l9 7 9-7"/></svg></span>
    <span class="icon"><svg viewBox="0 0 24 24"><circle cx="12" cy="12" r="9"/><path d="M3 12h18M12 3c3 3 3 15 0 18M12 3c-3 3-3 15 0 18"/></svg></span>
  </div>
  <div class="contact">
    <div>208-555-0193</div>
    <div>208-555-0147</div>
    <div>grangerearthworksllc@mailnest.example</div>
    <div>www.grangerearthworksllc.example</div>
  </div>
  <div class="rule"></div>
  <div class="address">
    <div>4587 Street Address Name</div>
    <div>Country Name AB 4581</div>
  </div>
</section>

<section class="card card-back" aria-label="Business card back">
  <div class="back-pattern" role="img" aria-label="Repeating faint pattern of mountain and excavator motifs"></div>
  <div class="back-brand"><span class="dot"></span>Granger Earthworks LLC</div>
  <ul class="services">
    <li>Driveways</li><li>Retaining Walls</li><li>Site Prep</li><br>
    <li>Septic Systems</li><li>Rock Delivery</li>
  </ul>
</section>

</body>
</html>
```